" A empresa funciona em um escritório físico, onde os clientes são recebidos para conversar sobre como desejam seu projeto residencial ou comercial. Oferecemos também projetos de decoração, e de instalações, bem como projeto de estrutura. O processo de criação se da tambem pela produção de projetos em 3d. alem da produção do projeto acompanhamos tambem a obra e todo o processo de construção. "

```html
<!DOCTYPE html>
<html lang="pt-BR">
<head>
<meta charset="UTF-8">
<title>Marina Teixeira — Arquitetura e Interiores</title>
<link rel="stylesheet" href="https://fonts.googleapis.com/css2?family=Montserrat:wght@300;400&display=swap">
<style>
  :root {
    --backdrop: #ecebe8;
    --card-grey: #8b8c8e;
    --grey-light: #a3a4a6;
    --brand-yellow: #ffd61f;
    --paper: #ffffff;
    --ink-grey: #7a7b7d;
  }
  html, body {
    margin: 0;
    width: 1200px;
    height: 1200px;
    overflow: hidden;
    background: var(--backdrop);
    font-family: "Montserrat", sans-serif;
  }
  .canvas {
    position: relative;
    width: 1200px;
    height: 1200px;
  }
  .card {
    position: absolute;
    left: 160px;
    width: 880px;
    height: 500px;
    overflow: hidden;
    box-shadow: 0 10px 30px rgba(0,0,0,0.12);
  }
  .card-front {
    top: 70px;
    background: var(--card-grey);
  }
  .card-back {
    top: 630px;
    background: var(--paper);
    border-top-right-radius: 250px;
  }
  .card-shape {
    position: absolute;
    inset: 0;
    width: 100%;
    height: 100%;
  }
  .front-identity {
    position: absolute;
    left: 90px;
    top: 200px;
    display: flex;
    align-items: center;
    gap: 26px;
  }
  .identity-dot {
    width: 22px;
    height: 22px;
    border-radius: 50%;
    background: var(--brand-yellow);
  }
  .front-name {
    margin: 0;
    color: var(--paper);
    font-weight: 300;
    font-size: 54px;
    letter-spacing: 5px;
    text-transform: uppercase;
  }
  .front-tagline {
    position: absolute;
    left: 138px;
    top: 280px;
    margin: 0;
    color: var(--brand-yellow);
    font-weight: 400;
    font-size: 19px;
    letter-spacing: 4px;
    text-transform: uppercase;
  }
  .contact-list {
    position: absolute;
    left: 70px;
    top: 70px;
    margin: 0;
    padding: 0;
    list-style: none;
    color: var(--ink-grey);
    font-weight: 300;
    font-size: 22px;
    line-height: 44px;
  }
  .contact-list li {
    display: flex;
    align-items: center;
    gap: 14px;
  }
  .contact-icon {
    width: 16px;
    height: 16px;
    flex: none;
  }
  .back-identity {
    position: absolute;
    left: 70px;
    bottom: 150px;
    display: flex;
    align-items: center;
    gap: 18px;
  }
  .back-name {
    margin: 0;
    color: var(--ink-grey);
    font-weight: 300;
    font-size: 34px;
    letter-spacing: 4px;
    text-transform: uppercase;
  }
  .back-identity .identity-dot {
    width: 18px;
    height: 18px;
  }
</style>
</head>
<body>
<main class="canvas">

  <section class="card card-front" aria-label="Frente do cartão">
    <svg class="card-shape" viewBox="0 0 880 500" aria-hidden="true">
      <rect x="0" y="0" width="880" height="500" fill="var(--card-grey)"/>
      <path d="M880 0 L880 500 L640 500 Q560 250 640 0 Z" fill="var(--grey-light)" opacity="0.45"/>
    </svg>
    <div class="front-identity">
      <span class="identity-dot"></span>
      <h1 class="front-name">Marina Teixeira</h1>
    </div>
    <p class="front-tagline">Arquitetura • Interiores</p>
  </section>

  <section class="card card-back" aria-label="Verso do cartão">
    <svg class="card-shape" viewBox="0 0 880 500" aria-hidden="true">
      <path d="M0 430 Q440 300 880 360 L880 500 L0 500 Z" fill="var(--brand-yellow)"/>
    </svg>
    <ul class="contact-list">
      <li>
        <svg class="contact-icon" viewBox="0 0 16 16" aria-hidden="true"><path d="M8 1a5 5 0 0 0-5 5c0 4 5 9 5 9s5-5 5-9a5 5 0 0 0-5-5zm0 7a2 2 0 1 1 0-4 2 2 0 0 1 0 4z" fill="var(--ink-grey)"/></svg>
        Pç. Antônio Ferreira Lima 210, sala 4
      </li>
      <li>
        <span class="contact-icon"></span>
        Centro • Vale Verde • Bahia
      </li>
      <li>
        <svg class="contact-icon" viewBox="0 0 16 16" aria-hidden="true"><path d="M4 1l3 3-2 2a9 9 0 0 0 5 5l2-2 3 3-2 3C7 15 1 9 1 3z" fill="var(--ink-grey)"/></svg>
        (75) 90123-4567 • 90765-4321
      </li>
      <li>
        <svg class="contact-icon" viewBox="0 0 16 16" aria-hidden="true"><rect x="1" y="3" width="14" height="10" rx="1" fill="none" stroke="var(--ink-grey)" stroke-width="1.5"/><path d="M1 4l7 5 7-5" fill="none" stroke="var(--ink-grey)" stroke-width="1.5"/></svg>
        marinaarquitetura@email.com
      </li>
    </ul>
    <div class="back-identity">
      <span class="identity-dot"></span>
      <p class="back-name">Marina Teixeira</p>
    </div>
  </section>

</main>
</body>
</html>
```